New minimal and cool business card

We have a brand new logo - we would like to use the logo on blue on the front of the card
The tagline is The give and take network (tm)
We would like information on the back of the card for individual(s)

Our font is Lato
Our colors are indicated in the attached identity guide which uses the old logo - we are de-emphasizing orange

Please prepare the artwork to meet the specs on this site
http://us.pirvex.com/products/sheen/business-cards.html

Front: Logo and tagline on dark blue

Back: On white
Join Today
http://ourtandem.co/join

```html
<!DOCTYPE html>
<html lang="en">
<head>
<meta charset="utf-8">
<title>ourtandem business card</title>
<link href="https://fonts.googleapis.com/css2?family=Lato:wght@300;400;700&display=swap" rel="stylesheet">
<style>
  :root {
    --bg: #2a2b2e;
    --card-white: #ffffff;
    --brand-blue: #34495e;
    --band-grey: #d9d9d9;
    --band-light: #ececec;
    --stripe-slate: #7d8b98;
    --stripe-mist: #e6e9ec;
    --ink: #3b4149;
    --ink-soft: #5e646b;
  }
  * { box-sizing: border-box; margin: 0; padding: 0; }
  html, body { width: 1200px; height: 864px; overflow: hidden; }
  body {
    background: var(--bg);
    font-family: "Lato", sans-serif;
    display: flex;
    align-items: center;
    justify-content: center;
    gap: 44px;
  }
  .card {
    width: 520px;
    height: 297px;
    position: relative;
    overflow: hidden;
    background: var(--card-white);
    box-shadow: 0 10px 30px rgba(0,0,0,.45);
  }
  .wordmark {
    font-weight: 400;
    letter-spacing: 1px;
    line-height: 1;
    white-space: nowrap;
  }

  /* Front face: white with grey url band */
  .card-front .wordmark {
    position: absolute;
    left: 0; right: 0; top: 82px;
    text-align: center;
    font-size: 46px;
    color: var(--brand-blue);
  }
  .card-front .url-band {
    position: absolute;
    left: 0; right: 0; top: 178px;
    height: 40px;
    background: var(--band-grey);
    display: flex;
    align-items: center;
    justify-content: center;
    font-size: 13px;
    letter-spacing: 3px;
    color: var(--ink-soft);
  }
  .card-front .under-band {
    position: absolute;
    left: 0; right: 0; top: 218px;
    height: 16px;
    background: var(--band-light);
  }

  /* Back face: blue panel, stripes, details */
  .card-back .brand-panel {
    position: absolute;
    left: 0; top: 0; bottom: 0;
    width: 236px;
    background: var(--brand-blue);
    display: flex;
    align-items: center;
    justify-content: center;
  }
  .card-back .brand-panel .wordmark {
    font-size: 34px;
    color: var(--card-white);
  }
  .card-back .stripe-slate {
    position: absolute;
    left: 236px; top: 0; bottom: 0;
    width: 34px;
    background: var(--stripe-slate);
  }
  .card-back .stripe-mist {
    position: absolute;
    left: 270px; top: 0; bottom: 0;
    width: 22px;
    background: var(--stripe-mist);
  }
  .details {
    position: absolute;
    left: 312px; top: 34px; right: 16px;
    color: var(--ink);
  }
  .person-name {
    font-size: 14px;
    font-weight: 400;
    letter-spacing: 1px;
    white-space: nowrap;
  }
  .person-title {
    font-size: 10px;
    letter-spacing: 1px;
    margin-top: 3px;
    color: var(--ink-soft);
  }
  .address {
    font-size: 11px;
    line-height: 1.45;
    margin-top: 30px;
  }
  .contacts {
    list-style: none;
    margin-top: 18px;
    font-size: 10px;
    color: var(--ink-soft);
  }
  .contacts li {
    display: flex;
    align-items: center;
    gap: 7px;
    margin-bottom: 6px;
    white-space: nowrap;
  }
  .contacts svg { width: 10px; height: 10px; fill: var(--ink); flex: none; }
</style>
</head>
<body>

  <section class="card card-front">
    <div class="wordmark">ourtandem</div>
    <div class="url-band">www.yoursitename.com</div>
    <div class="under-band"></div>
  </section>

  <section class="card card-back">
    <div class="brand-panel"><div class="wordmark">ourtandem</div></div>
    <div class="stripe-slate"></div>
    <div class="stripe-mist"></div>
    <div class="details">
      <div class="person-name">TESSA BRINDLOW</div>
      <div class="person-title">GENERAL MANAGER</div>
      <p class="address">214 Harbor Lane,<br>2nd Floor, Suite B</p>
      <ul class="contacts">
        <li><svg viewBox="0 0 10 10"><path d="M2 0.5 3.6 2.6 2.7 3.6C3.3 4.9 4.9 6.6 6.4 7.3L7.4 6.4 9.5 8 8.4 9.5C4.5 9.2 0.8 5.5 0.5 1.6Z"/></svg>012 555 0198</li>
        <li><svg viewBox="0 0 10 10"><path d="M2.5 0h5a1 1 0 0 1 1 1v8a1 1 0 0 1-1 1h-5a1 1 0 0 1-1-1V1a1 1 0 0 1 1-1Zm0.6 1.2v6.4h3.8V1.2Z"/></svg>012 555 0198</li>
        <li><svg viewBox="0 0 10 10"><path d="M2 3.5h6v5H2Zm1-3h4v2H3Zm0.5 5.5h3v1h-3Z"/></svg>012 555 0198</li>
        <li><svg viewBox="0 0 10 10"><path d="M0 2h10v6H0Zm1 0.8 4 2.8 4-2.8v-0.1H1Z"/></svg>yourname@mail.com</li>
        <li><svg viewBox="0 0 10 10"><path d="M5 0a5 5 0 1 0 0.01 0Zm0 1.2a3.8 3.8 0 1 1-0.01 0Z"/><path d="M1 4.5h8v1H1Zm3.5-4h1v9h-1Z"/></svg>www.yoursitename.com</li>
      </ul>
    </div>
  </section>

</body>
</html>
```